Amber Hollow Gathering - Promotional Poster

Amber Hollow Gathering is a party by the people, for the people. It’s where the grooviest group of creatives comes together to dream, connect, learn and inspire. This incredible forest-stomping celebration is returning in 2023 with our latest event “Velvet Jamboree”
We need your help to create consistent branding that will make the event memorable and recognisable to our attendees. To start with we need a poster announcing the festival theme and our artists for this year.
Here are the key elements we would like you to include in your design:
1. Theme: The branding should reflect the theme of "Velvet Jamboree" with vibrant colours, cosmic imagery, carnival imagery, and celestial elements. It should evoke a sense of wonder, excitement, and adventure.
2. Logo - It should include our Amber Hollow Logo. AI file attached.
3. Text - Amber Hollow (or logo) Presents Velvet Jamboree”
Must haves -
- The logo or festival name
- The Date 5-8th May 2023
- Location - Mudgee NSW
- ticket link www.amberhollowgathering.com
- artist names put in alphabetical order.
Marta Quillby
Pieter Renwold
Fig moss
Tobias Wrenfield
Murfolk
Rosie K
Nora F
Dominic Pryle
Ivo marrantes
Greta Vane
Hana P
Perdu
Vim Ostra
Otis R & Quen
4. Colour scheme: The colour scheme should be consistent with the theme of "Velvet Jamboree." We would like a range of bold and bright colours that reflect the colours of the cosmos such as purple, blue, and pink.
5. Typography: The typography should be clear and easy to read. We would like a font that reflects the Velvet Jamboree theme.
6. Graphical elements - The poster may include pictorial elements, stars, planets, moons, galaxies, carnival imagery.
7. Marketing collateral: For the winner of this project we need marketing collateral that is consistent with the branding, including artist tiles, posters, banners, social media graphics, and other promotional materials.
8. Deliverables - We need the .Ai .Id or photoshop files at the end of this project.
You can view videos & details of our past events at www.amberhollowgathering.com or on instagram.com/amber_hollow_gathering
We are excited to see your ideas and look forward to working with you

```html
<!DOCTYPE html>
<html lang="en">
<head>
<meta charset="utf-8">
<title>Amber Hollow Gathering – Velvet Jamboree Poster</title>
<link rel="stylesheet" href="https://fonts.googleapis.com/css2?family=Oswald:wght@200;300;400;500&display=swap">
<style>
  :root {
    --page-bg: #dcdcdc;
    --ink-white: #ffffff;
    --ink-teal: #4fc3cf;
    --rule-teal: #3a8f9a;
    --space-deep: #03080b;
    --space-mid: #0b2a33;
    --nebula: #3f9aa6;
    --nebula-glow: #a9e3ea;
  }
  * { box-sizing: border-box; margin: 0; padding: 0; }
  html, body {
    width: 1016px;
    height: 1200px;
    overflow: hidden;
    background: var(--page-bg);
  }
  .poster {
    position: absolute;
    left: 67px;
    top: 30px;
    width: 881px;
    height: 1140px;
    overflow: hidden;
    background: var(--space-deep);
    color: var(--ink-white);
    font-family: "Oswald", "Arial Narrow", sans-serif;
  }
  .poster__artwork {
    position: absolute;
    inset: 0;
    background:
      radial-gradient(ellipse 38% 30% at 52% 33%, rgba(169,227,234,0.55), transparent 70%),
      radial-gradient(circle 150px at 50% 47%, #0d1a22 0%, #0d1a22 92%, transparent 100%),
      radial-gradient(ellipse 60% 40% at 30% 25%, rgba(63,154,166,0.75), transparent 75%),
      radial-gradient(ellipse 45% 35% at 85% 60%, rgba(40,90,100,0.5), transparent 75%),
      linear-gradient(180deg, var(--space-mid) 0%, #0f3a44 35%, #0a2229 60%, var(--space-deep) 82%, #000 100%);
  }
  .poster__rules {
    position: absolute;
    inset: 0;
    width: 881px;
    height: 1140px;
  }
  .brand {
    position: absolute;
    top: 128px;
    left: 0;
    width: 881px;
    text-align: center;
    font-weight: 300;
    color: var(--ink-white);
  }
  .brand__name {
    font-size: 40px;
    letter-spacing: 10px;
    line-height: 1.1;
    padding-left: 10px;
  }
  .brand__sub {
    display: flex;
    justify-content: center;
    align-items: center;
    gap: 10px;
    font-size: 15px;
    letter-spacing: 10px;
    line-height: 1.6;
  }
  .brand__rule {
    width: 95px;
    height: 1px;
    background: var(--ink-white);
    opacity: 0.8;
  }
  .theme-title {
    position: absolute;
    left: 0;
    top: 238px;
    width: 881px;
    text-align: center;
    font-weight: 200;
    font-size: 168px;
    line-height: 1;
    letter-spacing: 30px;
    padding-left: 30px;
  }
  .theme-subtitle {
    position: absolute;
    right: 127px;
    top: 424px;
    font-weight: 400;
    font-size: 66px;
    line-height: 1;
    letter-spacing: 5px;
  }
  .event-date {
    position: absolute;
    right: 134px;
    top: 524px;
    font-weight: 400;
    font-size: 24px;
    line-height: 1;
    letter-spacing: 3px;
  }
  .lineup {
    position: absolute;
    top: 628px;
    left: 0;
    width: 881px;
    list-style: none;
    text-align: center;
    font-weight: 400;
    font-size: 21px;
    line-height: 25.8px;
    letter-spacing: 4px;
    text-transform: uppercase;
  }
  .location {
    position: absolute;
    top: 1046px;
    left: 0;
    width: 881px;
    text-align: center;
    font-weight: 400;
    font-size: 24px;
    letter-spacing: 2px;
    color: var(--ink-teal);
  }
  .ticket-link {
    position: absolute;
    top: 1088px;
    left: 0;
    width: 881px;
    display: flex;
    justify-content: center;
    align-items: center;
    gap: 20px;
    font-weight: 400;
    font-size: 15px;
    letter-spacing: 3px;
    color: var(--ink-teal);
    text-transform: uppercase;
  }
  .ticket-link__rule {
    width: 44px;
    height: 1.5px;
    background: var(--rule-teal);
  }
</style>
</head>
<body>
  <main class="poster">
    <div class="poster__artwork" role="img" aria-label="Teal cosmic nebula with a dark planet and small moon, a carnival masquerade mask at the right, and a silhouetted festival crowd along the bottom"></div>

    <svg class="poster__rules" viewBox="0 0 881 1140" aria-hidden="true">
      <line x1="0" y1="508" x2="756" y2="508" stroke="#4fa9b4" stroke-width="1.5" opacity="0.8"/>
      <line x1="360" y1="640" x2="880" y2="20" stroke="#9fdde4" stroke-width="1" opacity="0.45"/>
      <line x1="600" y1="600" x2="880" y2="260" stroke="#9fdde4" stroke-width="1" opacity="0.35"/>
      <line x1="230" y1="560" x2="640" y2="60" stroke="#9fdde4" stroke-width="1" opacity="0.3"/>
    </svg>

    <header class="brand">
      <p class="brand__name">AMBER HOLLOW</p>
      <p class="brand__sub"><span class="brand__rule"></span><span>GATHERING</span><span class="brand__rule"></span></p>
    </header>

    <h1 class="theme-title">VELVET</h1>
    <h2 class="theme-subtitle">JAMBOREE</h2>
    <p class="event-date">DATE 5-8TH MAY 2023</p>

    <ul class="lineup">
      <li>Dominic Pryle</li>
      <li>Fig moss</li>
      <li>Greta Vane</li>
      <li>Hana P</li>
      <li>Ivo marrantes</li>
      <li>Marta Quillby</li>
      <li>Murfolk</li>
      <li>Nora F</li>
      <li>Otis R &amp; Quen</li>
      <li>Perdu</li>
      <li>Pieter Renwold</li>
      <li>Rosie K</li>
      <li>Tobias Wrenfield</li>
      <li>Vim Ostra</li>
    </ul>

    <p class="location">MUDGEE NSW</p>
    <p class="ticket-link">
      <span class="ticket-link__rule"></span>
      <span>www.amberhollowgathering.com</span>
      <span class="ticket-link__rule"></span>
    </p>
  </main>
</body>
</html>
```